New product brochure for CEO's

We have created a research product that creates a syndicate of the CEO's from Australia's top 30 insurance firms. The purpose of the study is to ask CEO's to share their views on the future of the industry over the next 12 months.

The purpose of this flyer will be to email to CEO's an overview of the product prior to our company calling them to arrange a meeting. The purpose of the flyer will be to professionally and succintly lay out the concept and logistics of the new product.

Because CEO's are very time poor and often demanding people, we need a design that is simple but professional in appearance. From a design perspective, we naturally want the flyer to contain elements that reflect our company's master brand. We have included in the attachments copies of our company logo and business card. Please use these two elements to inspire your designs.

We want a clean design that does not contain any photographs or graphical images beyond any elements inspired by our company livery. The product is called the 'Summit Market Lens'. Ideally, the flyer would create a design for this title that reflects our 'kelp' brand, in particular the use of the 'double helix' that appears to the left hand side of the kelp brand name in our logo.

For your reference, our company RGB colours are:

Logo:
Grey- #6d6e70 (RGB – 109,110,112)
Green - #8cc63e (RGB – 140,198,62)
Blue - #1b75bb (RGB – 27,117,187)
Font - Helvetica Neue Bold

Word:
Font – Calibri
Size – 10
Line Spacing: 1.15 (Multiple)
Between Paragraphs: 8pt (After)

We require a double sided flyer. We have included a word document that reflects the amount of text that will need to be contained on both the front and reverse side of the flyer.

The second side of the flyer will contain a list of the products deliverables. In the word document that we have provided, we have represented this as a series of bullet points. Please feel free to use your creative flair to display this information in other formats. For example - tables or shaded areas, etc.

In your designs please consider that the target market (namely CEO's) are typically male businessmen aged over 50 years. So whilst we are looking for a contemporary and modern design, it must not alienate an older target audience.

Target Market(s)

CEO's of large insurance firms

Industry/Entity Type

Insurance

Font styles to use
Other font styles liked:
• Refer to main brief

Requirements
Must have
• - Must use our company colours (see above in description)
• - Must be clean, simple and professional
• - Must incorporate our logo
• - Must create a logo / graphical treatment for the product name 'Summit Market Lens'
• - Must provide sufficient space for text to be inserted within the document (as per attached example PDF file)
Should not have
• - Must not have any photographs

```html
<!DOCTYPE html>
<html lang="en">
<head>
<meta charset="utf-8">
<title>Summit Market Lens – Flyer</title>
<link href="https://fonts.googleapis.com/css2?family=Roboto+Condensed:ital,wght@0,300;0,400;0,700;1,700&family=Roboto:wght@300;400;700&display=swap" rel="stylesheet">
<style>
  :root{
    --brand-grey:#6d6e70;
    --brand-green:#8cc63e;
    --brand-blue:#1b75bb;
    --ink:#222;
    --stage:#1f4d74;
    --icon-grey:#b9babc;
    --sky:#bfe7f3;
  }
  *{box-sizing:border-box;margin:0;padding:0}
  html,body{width:1200px;height:1200px;overflow:hidden}
  body{background:var(--stage);font-family:"Roboto Condensed",Arial,sans-serif;color:var(--ink);position:relative}

  .sheet{position:absolute;width:570px;height:735px;background:#fff;overflow:hidden}
  .sheet--front{left:20px;top:40px;
    background:linear-gradient(160deg,var(--sky) 0%,#e9f7fb 22%,#fff 40%,#fff 70%,#dff2f8 100%)}
  .sheet--back{left:610px;top:425px;
    background:linear-gradient(200deg,var(--sky) 0%,#eef9fc 25%,#fff 45%,#fff 80%,#d6f0f7 100%)}

  .product-name{font-family:"Roboto Condensed",Arial,sans-serif;font-weight:700;color:var(--brand-blue);line-height:1}
  .product-name .big{display:block;font-size:66px;letter-spacing:1px}
  .product-name .small{display:block;font-size:28px}

  .sheet--front .product-name{position:absolute;right:44px;top:38px;text-align:right}
  .tagline{position:absolute;right:28px;top:170px;font-family:"Roboto",Arial,sans-serif;font-weight:300;font-size:21px;color:#333}
  .intro{position:absolute;left:30px;right:28px;top:205px;text-align:right;font-size:12.2px;line-height:1.3;color:#222}

  .columns{position:absolute;left:36px;right:26px;top:272px;display:flex;gap:14px}
  .column{flex:1}
  .column-icon{display:block;margin:0 auto 4px;width:80px;height:80px}
  .column-title{text-align:center;font-family:"Roboto",Arial,sans-serif;font-weight:300;font-size:18px;color:var(--brand-grey);margin-bottom:6px}
  .column p{font-size:7.6px;line-height:1.4;text-align:justify;margin-bottom:9px;color:#222}

  .front-wave{position:absolute;left:0;bottom:0;width:570px;height:175px}
  .brand-disc{position:absolute;display:flex;align-items:center;justify-content:center;background:#fff;border-radius:50%}
  .brand-name{font-family:"Roboto Condensed",Arial,sans-serif;font-weight:700;color:var(--brand-blue);letter-spacing:-1px}
  .sheet--front .brand-disc{left:392px;top:574px;width:100px;height:100px}
  .sheet--front .brand-name{font-size:36px}
  .front-contact{position:absolute;left:0;right:36px;bottom:30px;text-align:right;color:#fff;font-size:17px;font-weight:300;word-spacing:14px}
  .front-contact span{word-spacing:0}

  .back-band{position:absolute;left:0;top:0;width:570px;height:735px}
  .sheet--back .product-name{position:absolute;left:165px;top:52px;display:flex;align-items:flex-end;gap:10px}
  .sheet--back .product-name .big{font-size:64px}
  .sheet--back .product-name .small{font-size:24px;line-height:1.05;padding-bottom:6px}
  .back-content{position:absolute;left:176px;right:30px;top:150px}
  .section-title{font-family:"Roboto",Arial,sans-serif;font-weight:300;font-size:29px;color:#222;margin-bottom:4px}
  .section-lead{font-size:11.2px;line-height:1.25;color:#222;margin-bottom:12px}
  .deliverables{list-style:none;margin-bottom:14px}
  .deliverables li{position:relative;padding-left:22px;font-size:13.5px;line-height:1.45;color:#222}
  .deliverables li::before{content:"";position:absolute;left:4px;top:4px;width:6px;height:10px;
    border-right:3px solid var(--brand-blue);border-bottom:3px solid var(--brand-blue);transform:rotate(40deg)}
  .closing{font-weight:700;font-style:italic;font-size:13px;line-height:1.25;color:#111;margin-top:4px}
  .sheet--back .brand-disc{left:40px;top:540px;width:96px;height:96px}
  .sheet--back .brand-name{font-size:32px}
  .back-contact{position:absolute;left:30px;top:652px;color:#fff;font-size:12.5px;line-height:1.35}
</style>
</head>
<body>

<section class="sheet sheet--front">
  <h1 class="product-name"><span class="big">Summit</span><span class="small">Market Lens</span></h1>
  <p class="tagline">Australia's top 30 insurance firms</p>
  <p class="intro">The purpose of this flyer will be to email to CEO's an overview of the product prior to our company calling them to arrange a meeting. The purpose of the flyer will be to professionally and succintly lay out the concept and logistics of the new product.</p>

  <div class="columns">
    <article class="column">
      <svg class="column-icon" viewBox="0 0 80 80" aria-hidden="true">
        <circle cx="40" cy="40" r="38" fill="var(--icon-grey)"/>
        <path d="M22 42 L35 55 L60 24" fill="none" stroke="#fff" stroke-width="9" stroke-linecap="round" stroke-linejoin="round"/>
      </svg>
      <h2 class="column-title">Benefits</h2>
      <p>Kelp is a next generation market research firm. We combine our expertise in traditional market research with the benefits offered by modern technology, to provide our clients with ROI focused insights.</p>
      <p>We do this by collecting traditional research data via leading edge online survey techniques and focus groups, and then where applicable, combining them with internal customer, product or service data.</p>
      <p>Our innovative approach to research uses traditional theories to explain 'why and how' customers are making decisions, in conjunction with client data to demonstrate 'what' impact these decisions are having upon actual sales performance.</p>
      <p>The analyses that we conduct are thorough, but the work we produce is simple to digest, not to mention highly effective in helping clients to make better commercial decisions.</p>
    </article>
    <article class="column">
      <svg class="column-icon" viewBox="0 0 80 80" aria-hidden="true">
        <circle cx="40" cy="40" r="38" fill="var(--icon-grey)"/>
        <g fill="#fff">
          <circle cx="48" cy="32" r="13"/>
          <g stroke="#fff" stroke-width="6">
            <line x1="48" y1="14" x2="48" y2="50"/><line x1="30" y1="32" x2="66" y2="32"/>
            <line x1="35" y1="19" x2="61" y2="45"/><line x1="61" y1="19" x2="35" y2="45"/>
          </g>
          <circle cx="28" cy="54" r="8"/>
          <g stroke="#fff" stroke-width="4">
            <line x1="28" y1="42" x2="28" y2="66"/><line x1="16" y1="54" x2="40" y2="54"/>
            <line x1="20" y1="46" x2="36" y2="62"/><line x1="36" y1="46" x2="20" y2="62"/>
          </g>
        </g>
        <circle cx="48" cy="32" r="5" fill="var(--icon-grey)"/>
        <circle cx="28" cy="54" r="3" fill="var(--icon-grey)"/>
      </svg>
      <h2 class="column-title">Process</h2>
      <p>Kelp is a next generation market research firm. We combine our expertise in traditional market research with the benefits offered by modern technology, to provide our clients with ROI focused insights.</p>
      <p>We do this by collecting traditional research data via leading edge online survey techniques and focus groups, and then where applicable, combining them with internal customer, product or service data.</p>
      <p>Our innovative approach to research uses traditional theories to explain 'why and how' customers are making decisions, in conjunction with client data to demonstrate 'what' impact these decisions are having upon actual sales performance.</p>
    </article>
    <article class="column">
      <svg class="column-icon" viewBox="0 0 80 80" aria-hidden="true">
        <circle cx="40" cy="40" r="38" fill="var(--icon-grey)"/>
        <text x="40" y="56" text-anchor="middle" font-family="Roboto, Arial, sans-serif" font-weight="700" font-size="40" fill="#fff">$</text>
      </svg>
      <h2 class="column-title">Investment</h2>
      <p>Kelp is a next generation market research firm. We combine our expertise in traditional market research with the benefits offered by modern technology, to provide our clients with ROI focused insights.</p>
      <p>We do this by collecting traditional research data via leading edge online survey techniques and focus groups, and then where applicable, combining them with internal customer, product or service data.</p>
      <p>Our innovative approach to research uses traditional theories to explain 'why and how' customers are making decisions, in conjunction with client data</p>
    </article>
  </div>

  <svg class="front-wave" viewBox="0 0 570 175" preserveAspectRatio="none" aria-hidden="true">
    <defs>
      <linearGradient id="frontBlue" x1="0" y1="0" x2="0" y2="1">
        <stop offset="0" stop-color="#5fc0df"/><stop offset="1" stop-color="var(--brand-blue)"/>
      </linearGradient>
    </defs>
    <path d="M0 110 C160 60 360 10 570 0 L570 40 C380 50 180 100 0 150 Z" fill="var(--brand-green)"/>
    <path d="M0 130 C170 80 370 30 570 28 L570 175 L0 175 Z" fill="url(#frontBlue)"/>
  </svg>
  <div class="brand-disc"><span class="brand-name">kelp</span></div>
  <p class="front-contact"><span>info@kelpinsights.com.au</span> <span>www.kelpinsights.com.au</span></p>
</section>

<section class="sheet sheet--back">
  <svg class="back-band" viewBox="0 0 570 735" preserveAspectRatio="none" aria-hidden="true">
    <defs>
      <linearGradient id="backBand" x1="0" y1="0" x2="0" y2="1">
        <stop offset="0" stop-color="var(--brand-green)"/>
        <stop offset="0.35" stop-color="#5aa89a"/>
        <stop offset="1" stop-color="var(--brand-blue)"/>
      </linearGradient>
    </defs>
    <path d="M0 0 L110 0 C150 200 160 450 190 735 L0 735 Z" fill="url(#backBand)"/>
    <path d="M110 0 L140 0 C170 220 180 460 205 735 L190 735 C160 450 150 200 110 0 Z" fill="#e3efe8"/>
  </svg>

  <h1 class="product-name"><span class="big">Summit</span><span class="small">Market<br>Lens</span></h1>

  <div class="back-content">
    <h2 class="section-title">Core Metrics</h2>
    <p class="section-lead">Our innovative approach to research uses traditional theories to explain 'why and how' customers are making decisions, in conjunction with client data to demonstrate 'what' impact these decisions are having upon actual sales performance.</p>
    <ul class="deliverables">
      <li>The purpose of this flyer</li>
      <li>Will be to email to CEO's an</li>
      <li>Overview of the product</li>
      <li>Prior to our company</li>
      <li>Calling them to arrange a</li>
      <li>Meeting. The purpose of</li>
    </ul>
    <h2 class="section-title">Core Metrics</h2>
    <p class="section-lead">The analyses that we conduct are thorough, but the work we produce is simple to digest, not to mention highly effective in helping clients to make better commercial decisions.</p>
    <ul class="deliverables">
      <li>The purpose of this flyer</li>
      <li>Will be to email to CEO's an</li>
      <li>Overview of the product</li>
      <li>Prior to our company</li>
      <li>Calling them to arrange a</li>
      <li>Meeting. The purpose of</li>
    </ul>
    <p class="closing">We utilise the latest dashboard technology to deliver end reports that are both visually appealing and interactive.</p>
  </div>

  <div class="brand-disc"><span class="brand-name">kelp</span></div>
  <p class="back-contact">info@kelpinsights.com.au<br>www.kelpinsights.com.au</p>
</section>

</body>
</html>
```